Business cards for a tribute and obituary website

Our website is called Tribute Lantern.

It is a special place online for people to remember their loved ones who have passed away, through obituaries and tributes. Friends and family can also convey their condolences on the deceased's memorial page. Celebrating the life of the deceased and remembering their legacy is very important to us – death should not be just about grieving.

We would like the card to look tasteful and modern. The design should ideally not have colours that are too bright. The logo and website URL, www.tributelantern.example should be visible on the front of the card, with our slogan "Celebrating a life passed" on the back.

The design should communicate our purpose – remembering loved ones who have passed – and also a lighter tone of celebrating life. It should not look like a funeral director's card!

Our logo has been attached. Looking forward to some beautiful designs! Get creative :)
Updates

Project Deadline Extended
Reason: Thank you all for your designs. The rest of my team and I have not reached a decision on which design to select and I am collecting feedback from them. I will provide feedback for any changes that need to be made soon. It would be great if we could see more original designs and in more colours! We will definitely select a design by this deadline.

Industry/Entity Type

Business

Contact Information for Business Card

Wendy Lumb
Project Manager
614772390
wendylumb@tributelantern.example

Font styles to use
Serif
Sans Serif

Requirements
Must have
• Logo and website address (www.tributelantern.example) on the front.
Nice to have
• Hi designers! It would be nice to see alternative colours – feel free to try out colours that are tasteful and subtle. The colour of the business card does not have to be the same as the logo.
• We would also like to see the logo used in different ways, perhaps a glossy or embossed finish. The card should look stylish.

```html
<!DOCTYPE html>
<html lang="en">
<head>
<meta charset="utf-8">
<title>Tribute Lantern – Business Cards</title>
<link rel="stylesheet" href="https://fonts.googleapis.com/css2?family=Bitter:wght@700&family=Cinzel:wght@400;600&family=Quattrocento:wght@400&display=swap">
<style>
  :root {
    --backdrop: #34424a;
    --ink-navy: #1c4b69;
    --brand-blue: #0f67a0;
    --arc-blue: #6aa3c7;
    --card-white: #f7fbff;
    --card-mist: #bcd6ef;
    --text-light: #e8f2fa;
    --rule-light: #a9cbe4;
  }
  * { box-sizing: border-box; margin: 0; padding: 0; }
  html, body { width: 1200px; height: 900px; overflow: hidden; }
  body {
    background: var(--backdrop);
    position: relative;
  }
  .card {
    position: absolute;
    left: 250px;
    width: 700px;
    height: 400px;
    overflow: hidden;
    border-radius: 3px;
    box-shadow: 0 10px 30px rgba(0,0,0,0.35);
  }
  .card--back {
    top: 40px;
    background: radial-gradient(ellipse at 55% 45%, var(--card-white) 0%, #e6f0fa 40%, var(--card-mist) 100%);
  }
  .card--front {
    top: 470px;
    background: radial-gradient(ellipse at 25% 50%, var(--card-white) 0%, #e4eef8 60%, #c9def1 100%);
  }

  /* back */
  .slogan {
    position: absolute;
    top: 112px;
    left: 0;
    width: 100%;
    text-align: center;
    font-family: "Cinzel", serif;
    font-weight: 400;
    font-size: 40px;
    letter-spacing: 1px;
    color: var(--ink-navy);
  }
  .slogan-rule {
    position: absolute;
    top: 184px;
    left: 165px;
    width: 370px;
    height: 1.5px;
    background: var(--ink-navy);
  }
  .back-dot {
    position: absolute;
    top: 212px;
    left: 334px;
    width: 32px;
    height: 32px;
    border-radius: 50%;
    background: var(--ink-navy);
  }

  /* front */
  .front-shapes { position: absolute; inset: 0; }
  .brand {
    position: absolute;
    left: 40px;
    top: 60px;
    width: 250px;
    text-align: center;
  }
  .brand-dot {
    width: 110px;
    height: 110px;
    margin: 0 auto 22px;
    border-radius: 50%;
    background: var(--ink-navy);
  }
  .brand-name {
    font-family: "Bitter", serif;
    font-weight: 700;
    font-size: 36px;
    line-height: 1.05;
    color: var(--ink-navy);
  }
  .website {
    position: absolute;
    left: 42px;
    bottom: 32px;
    font-family: "Quattrocento", serif;
    font-size: 22px;
    color: var(--ink-navy);
  }
  .contact-head {
    position: absolute;
    left: 470px;
    top: 30px;
    width: 200px;
    text-align: center;
    color: var(--text-light);
  }
  .person-name {
    font-family: "Cinzel", serif;
    font-size: 25px;
    line-height: 1.1;
  }
  .person-role {
    font-family: "Cinzel", serif;
    font-weight: 600;
    font-size: 11px;
    letter-spacing: 0.5px;
  }
  .contact-rule {
    width: 176px;
    height: 1px;
    margin: 10px auto 8px;
    background: var(--rule-light);
  }
  .ornament {
    width: 34px;
    height: 12px;
    margin: 0 auto;
    border-radius: 6px;
    background: var(--arc-blue);
  }
  .email {
    position: absolute;
    left: 440px;
    top: 175px;
    width: 260px;
    text-align: center;
    font-family: "Quattrocento", serif;
    font-size: 15px;
    color: var(--text-light);
  }
  .phone {
    position: absolute;
    right: 42px;
    bottom: 42px;
    display: flex;
    align-items: center;
    gap: 14px;
    font-family: "Quattrocento", serif;
    font-size: 24px;
    letter-spacing: 1px;
    color: var(--text-light);
  }
  .phone-icon { width: 28px; height: 24px; }
</style>
</head>
<body>

  <section class="card card--back" aria-label="Card back">
    <h2 class="slogan">Celebrating a Life Passed</h2>
    <div class="slogan-rule"></div>
    <div class="back-dot"></div>
  </section>

  <section class="card card--front" aria-label="Card front">
    <svg class="front-shapes" width="700" height="400" viewBox="0 0 700 400" aria-hidden="true">
      <path d="M392 0 C 320 110, 340 300, 470 400 L 492 400 C 370 300, 352 120, 418 0 Z" fill="var(--arc-blue)"/>
      <path d="M440 0 C 380 110, 410 300, 560 400 L 700 400 L 700 0 Z" fill="var(--brand-blue)"/>
    </svg>

    <div class="brand">
      <div class="brand-dot"></div>
      <h1 class="brand-name">Tribute<br>Lantern</h1>
    </div>
    <p class="website">www.tributelantern.example</p>

    <div class="contact-head">
      <p class="person-name">Wendy Lumb</p>
      <p class="person-role">Project Manager</p>
      <div class="contact-rule"></div>
      <div class="ornament" role="img" aria-label="Small flourish ornament"></div>
    </div>

    <p class="email">wendylumb@tributelantern.example</p>

    <p class="phone">
      <svg class="phone-icon" viewBox="0 0 28 24" aria-hidden="true">
        <path d="M2 8 Q14 0 26 8 L23 11 L19 9 L19 7 Q14 5 9 7 L9 9 L5 11 Z" fill="var(--arc-blue)"/>
        <rect x="5" y="12" width="18" height="11" rx="2" fill="var(--arc-blue)"/>
        <circle cx="14" cy="17.5" r="3.2" fill="var(--brand-blue)"/>
      </svg>
      <span>614.772.390</span>
    </p>
  </section>

</body>
</html>
```